RUXO9 biz card & Stationery

UXO9 is a personalized shopping experience brought to you, that lets you find and discover fashion goods through a collection of boutiques curated by taste-makers - celebrities, stylists, designers, and fashion bloggers. Boutiques uses visual technology to help fashionistas discover and shop their look and creates the opportunity for designers to showcase their collections and latest inspirations online.

RUXO9 is built on technology developed by our team of fashion experts who work with engineers to “teach” our computer systems to understand various patterns, pairings, and genre definitions. When signed into your account, RUXO9 learns about your style and preferences and in turn, provides you better results and recommendations over time. Ultimately, RUXO9 will provide shoppers with a much richer and interactive shopping experience and help drive traffic to retailers' websites.

We need a definitely cool business card. The card must be black! And must use our official logo which can be download from RUXO9.com

The address for Letter head and evenlop, please use 4821 Larkmoor Avenue, Sutie 520 Los Angeles CA90012, email will be anyone@RUXO9.com, website is www.RUXO9.com

thanks

We received some of the design, thanks. But most of the design are not what we want. We need a very clean version with black ground, you may also use some dark gray to add the element. please take a look at http://bleckvorn.no/work/#tarvik__olmstrup/, we do like this kind of design very much. hope it help.

```html
<!DOCTYPE html>
<html lang="en">
<head>
<meta charset="utf-8">
<title>RUXO9 Business Card</title>
<link rel="stylesheet" href="https://fonts.googleapis.com/css2?family=Tenor+Sans&display=swap">
<style>
  :root {
    --backdrop: #8c8c8c;
    --card: #000000;
    --logo: #ffffff;
    --ghost: #242424;
    --band: #3a3a3a;
    --url: #3b3b3b;
    --contact: #b5b5b5;
  }
  html, body {
    margin: 0;
    width: 1200px;
    height: 900px;
    overflow: hidden;
    background: var(--backdrop);
    font-family: "Tenor Sans", sans-serif;
  }
  .canvas {
    position: relative;
    width: 1200px;
    height: 900px;
  }
  .card {
    position: absolute;
    top: 109px;
    width: 373px;
    height: 673px;
    display: block;
  }
  .card--front { left: 223px; }
  .card--back { left: 619px; }
  .card-ground { fill: var(--card); }
  .band { stroke: var(--band); stroke-width: 11; stroke-opacity: 0.45; }
  .ghost-name { fill: var(--ghost); font-size: 96px; }
  .brand-name { fill: var(--logo); font-size: 49px; }
  .site-url { fill: var(--url); font-size: 33px; letter-spacing: 1px; }
  .contact { fill: var(--contact); font-size: 18px; }
</style>
</head>
<body>
<main class="canvas">

  <svg class="card card--front" viewBox="0 0 373 673" aria-label="Business card front">
    <defs>
      <clipPath id="front-clip"><rect width="373" height="673"/></clipPath>
    </defs>
    <g clip-path="url(#front-clip)">
      <rect class="card-ground" width="373" height="673"/>
      <g class="bands">
        <line class="band" x1="0" y1="420" x2="420" y2="0"/>
        <line class="band" x1="0" y1="444" x2="444" y2="0"/>
        <line class="band" x1="0" y1="470" x2="470" y2="0"/>
        <line class="band" x1="0" y1="518" x2="518" y2="0"/>
        <line class="band" x1="0" y1="544" x2="544" y2="0"/>
        <line class="band" x1="0" y1="596" x2="596" y2="0"/>
        <line class="band" x1="0" y1="622" x2="622" y2="0"/>
      </g>
      <text class="ghost-name" x="-62" y="558">RUXO9</text>
      <text class="ghost-name" x="48" y="650">RUXO9</text>
      <text class="site-url" transform="translate(52 500) rotate(-90)">www.RUXO9.com</text>
      <text class="brand-name" x="349" y="73" text-anchor="end">RUXO9</text>
    </g>
  </svg>

  <svg class="card card--back" viewBox="0 0 373 673" aria-label="Business card back">
    <defs>
      <clipPath id="back-clip"><rect width="373" height="673"/></clipPath>
    </defs>
    <g clip-path="url(#back-clip)">
      <rect class="card-ground" width="373" height="673"/>
      <g class="bands">
        <line class="band" x1="0" y1="140" x2="140" y2="0"/>
        <line class="band" x1="0" y1="164" x2="164" y2="0"/>
        <line class="band" x1="0" y1="212" x2="212" y2="0"/>
        <line class="band" x1="0" y1="238" x2="238" y2="0"/>
        <line class="band" x1="0" y1="290" x2="290" y2="0"/>
        <line class="band" x1="0" y1="316" x2="316" y2="0"/>
      </g>
      <text class="ghost-name" x="41" y="144">RUXO9</text>
      <text class="ghost-name" x="178" y="191">RUXO9</text>
      <g class="contact-block" text-anchor="end">
        <text class="contact" x="345" y="596">4821 Larkmoor Avenue,</text>
        <text class="contact" x="345" y="620">Sutie 520 Los Angeles CA90012,</text>
        <text class="contact" x="345" y="644">e.: anyone@RUXO9.com</text>
      </g>
    </g>
  </svg>

</main>
</body>
</html>
```